Tavrel Fitness business cards

I need a business card for my company called Tavrel Fitness. I am a certified personal trainer, QMB certified, Hippo Pilates certified, and Vital paths certified. I am also an independent KORVEL rep, the number #1 rated nutritional and supplement product in the country. The card needs to convey Health, Wellness, Living Life and Loving It. I want it to be clean, sharp, eye-catching. Tantalizing.
Updates

for some reason, I'm unable to upload the pics I need. Stay tuned..

Industry/Entity Type

Business

Contact Information for Business Card

Tavrel Fitness
Mona Lykkestad, Owner
mona@tavrelfitness-example.com
555-203-4471
tavrelfitness-example.com
mona@tavrelfitness-example.com

Font styles to use
Serif

Requirements
Must have
• Must use pic of me and KORVEL logo

```html
<!DOCTYPE html>
<html lang="en">
<head>
<meta charset="utf-8">
<title>Tavrel Fitness business cards</title>
<link href="https://fonts.googleapis.com/css2?family=Crimson+Text:wght@400;600&display=swap" rel="stylesheet">
<style>
  :root {
    --page-bg: #f3f3f4;
    --card-bg: #ffffff;
    --navy: #1f3a78;
    --navy-band: #1f3f7c;
    --sky: #7ab3e3;
    --mark-blue: #3a84c9;
    --mark-grey: #9ea3a8;
    --photo-top: #d3dde2;
    --photo-bottom: #b9c7cf;
    --white: #ffffff;
  }
  * { margin: 0; padding: 0; box-sizing: border-box; }
  html, body {
    width: 1200px; height: 1000px; overflow: hidden;
    background: var(--page-bg);
    font-family: "Crimson Text", "Times New Roman", serif;
    color: var(--navy);
  }
  .stage { position: relative; width: 1200px; height: 1000px; }
  .card {
    position: absolute;
    width: 341px; height: 581px;
    background: var(--card-bg);
    overflow: hidden;
    box-shadow: 0 2px 6px rgba(0,0,0,0.12);
    text-align: center;
  }
  .card--front { left: 183px; top: 206px; }
  .card--back { left: 679px; top: 204px; height: 582px; }
  .line { position: absolute; left: 0; width: 100%; white-space: nowrap; }

  /* Front */
  .brand-mark {
    position: absolute; left: 124px; top: 34px;
    width: 94px; height: 94px; border-radius: 50%;
    background: var(--mark-blue);
  }
  .brand-name {
    top: 126px; font-size: 26px; line-height: 30px;
    color: var(--mark-grey); letter-spacing: 1px;
  }
  .front-title { top: 172px; font-size: 29px; line-height: 34px; }
  .front-wave { position: absolute; left: 0; top: 212px; width: 341px; height: 14px; }
  .portrait {
    position: absolute; left: 0; top: 223px; width: 341px; height: 358px;
    background: linear-gradient(180deg, var(--photo-top), var(--photo-bottom));
  }

  /* Back */
  .back-title { top: 74px; font-size: 27px; line-height: 34px; }
  .owner-role { top: 143px; font-size: 16px; line-height: 20px; }
  .owner-name { top: 166px; font-size: 24px; line-height: 30px; }
  .owner-email { top: 205px; font-size: 17px; line-height: 22px; }
  .owner-phone { top: 226px; font-size: 17px; line-height: 22px; }
  .owner-phone svg { width: 13px; height: 13px; vertical-align: -1px; margin-right: 3px; }
  .credentials {
    position: absolute; left: 0; top: 289px; width: 341px; height: 232px;
    background: var(--sky);
  }
  .credentials-wave { position: absolute; left: 0; top: -12px; width: 341px; height: 14px; }
  .credentials ul { list-style: none; padding-top: 16px; }
  .credentials li { font-size: 16.5px; line-height: 20px; margin-bottom: 11.3px; }
  .credentials li.claim { margin-bottom: 0; }
  .site-band {
    position: absolute; left: 0; bottom: 0; width: 341px; height: 62px;
    background: var(--navy-band); color: var(--white);
    font-size: 20px; line-height: 62px;
  }
</style>
</head>
<body>
<main class="stage">
  <section class="card card--front">
    <div class="brand-mark"></div>
    <div class="line brand-name">KORVEL</div>
    <div class="line front-title">Tavrel Fitness</div>
    <svg class="front-wave" viewBox="0 0 341 14" preserveAspectRatio="none">
      <path d="M0 2 C120 0 230 4 341 8 L341 14 L0 14 Z" fill="var(--sky)"/>
    </svg>
    <div class="portrait" role="img" aria-label="Portrait photo of the trainer, Mona Lykkestad"></div>
  </section>

  <section class="card card--back">
    <div class="line back-title">Tavrel Fitness</div>
    <div class="line owner-role">Owner</div>
    <div class="line owner-name">Mona Lykkestad</div>
    <div class="line owner-email">mona@tavrelfitness-example.com</div>
    <div class="line owner-phone"><svg viewBox="0 0 16 16"><path d="M3 1 L6 4 L4.5 6 C5.5 8.5 7.5 10.5 10 11.5 L12 10 L15 13 L13 15 C7 15 1 9 1 3 Z" fill="var(--navy)"/></svg>555-203-4471</div>
    <div class="credentials">
      <svg class="credentials-wave" viewBox="0 0 341 14" preserveAspectRatio="none">
        <path d="M0 3 C100 2 170 -1 240 4 C280 7 310 8 341 7 L341 14 L0 14 Z" fill="var(--sky)"/>
      </svg>
      <ul>
        <li>Certified Personal Trainer</li>
        <li>QMB certified</li>
        <li>Hippo Pilates certified</li>
        <li>Vital paths certified</li>
        <li>Independent KORVEL Rep</li>
        <li class="claim">Number #1 rated nutritional and<br>supplement product in the country</li>
      </ul>
    </div>
    <div class="site-band">tavrelfitness-example.com</div>
  </section>
</main>
</body>
</html>
```